A4 Flyer Design outlining our financial philosophy

One A4 page design (landscape orientation) outlining our financial philosophy.
The design needs to show these steps as the building blocks and the path taken to financial success:
1. Maximise income and reduce expenses
2. Maximise savings and reduce bad debts
3. Invest wisely & tax effectively
4. Manage risk
5. Plan for retirement
6. Leave a legacy
The design needs to incorporate the 6 building blocks above along with the key points for each topic. More info attached.
Design must be engaging, professional and consistent with our current branding colours.

Target Market(s)

self employed individuals looking to build wealth through property and shares.

Industry/Entity Type

Financial Planning

Font styles to use
Sans Serif

Colors
0255a3
5c5c5c
000000
ffffff

Requirements
Must have
• clear and engaging.
• consistent with current branding
• 6 topics with key considerations (as per attached)
• must show that all 6 points are linked and are a journey.

```html
<!DOCTYPE html>
<html lang="en">
<head>
<meta charset="utf-8">
<title>Our Financial Philosophy – Kindred Financial Group</title>
<link rel="stylesheet" href="https://fonts.googleapis.com/css2?family=Heebo:wght@500;700&display=swap">
<style>
  :root {
    --page: #ffffff;
    --blue-deep: #1f45a6;
    --blue-mid: #2f62c4;
    --blue-light: #4a7fd6;
    --band: #a9d3f5;
    --line: #ffffff;
    --text: #ffffff;
  }
  * { margin: 0; padding: 0; box-sizing: border-box; }
  html, body { width: 1200px; height: 881px; overflow: hidden; background: var(--page); }
  body { position: relative; font-family: "Heebo", Arial, sans-serif; color: var(--text); }

  .flyer { position: absolute; left: 54px; top: 54px; width: 1092px; height: 772px; overflow: hidden; }
  .flyer-photo {
    position: absolute; inset: 0;
    background:
      radial-gradient(ellipse at 75% 30%, rgba(120,160,235,.45), transparent 55%),
      radial-gradient(ellipse at 20% 10%, rgba(20,50,140,.7), transparent 50%),
      linear-gradient(160deg, var(--blue-deep) 0%, var(--blue-mid) 45%, var(--blue-light) 75%, var(--blue-mid) 100%);
  }

  .brand { position: absolute; right: 56px; top: 90px; display: flex; align-items: center; gap: 12px; }
  .brand-dot { width: 34px; height: 34px; border-radius: 50%; background: var(--text); }
  .brand-name { font-weight: 700; font-size: 26px; line-height: 1; }

  .journey { position: absolute; left: 0; top: 0; width: 1092px; height: 772px; }
  .step-title {
    position: absolute; width: 132px; text-align: center;
    font-weight: 700; font-size: 20px; line-height: 21px;
    transform: translate(-50%, -50%);
  }

  .points { position: absolute; top: 442px; list-style: none; font-weight: 500; font-size: 14px; line-height: 17px; }
  .points li { position: relative; padding-left: 10px; margin-bottom: 7px; }
  .points li::before { content: "•"; position: absolute; left: 0; }

  .band { position: absolute; left: 0; top: 719px; width: 1092px; height: 14px; }
  .site { position: absolute; left: 894px; top: 715px; font-weight: 500; font-size: 15.5px; }
</style>
</head>
<body>
<main class="flyer">
  <div class="flyer-photo" role="img" aria-label="Blue-tinted photo of hands working over financial charts and reports with a pen and tablet"></div>

  <div class="brand">
    <span class="brand-dot"></span>
    <span class="brand-name">Kindred Financial Group</span>
  </div>

  <svg class="journey" viewBox="0 0 1092 772" aria-hidden="true">
    <g fill="none" stroke="var(--line)" stroke-width="1.6">
      <polygon points="137,210 219,258 219,354 137,402 55,354 55,258"/>
      <polygon points="301,210 383,258 383,354 301,402 219,354 219,258"/>
      <polygon points="464,210 546,258 546,354 464,402 382,354 382,258"/>
      <polygon points="628,210 710,258 710,354 628,402 546,354 546,258"/>
      <polygon points="791,210 873,258 873,354 791,402 709,354 709,258"/>
      <polygon points="954,210 1036,258 1036,354 954,402 872,354 872,258"/>
    </g>
  </svg>

  <div class="step-title" style="left:135px;top:300px;width:130px">Maximise income and reduce expenses</div>
  <div class="step-title" style="left:301px;top:304px;width:130px">Maximise savings and reduce bad debts</div>
  <div class="step-title" style="left:464px;top:304px;width:120px">Invest wisely &amp; tax effectively</div>
  <div class="step-title" style="left:628px;top:306px;width:100px">Manage risk</div>
  <div class="step-title" style="left:803px;top:306px;width:120px">Plan for retirement</div>
  <div class="step-title" style="left:954px;top:306px;width:100px">Leave a legacy</div>

  <ul class="points" style="left:64px;width:160px">
    <li>Invest in yourself through education and training</li>
    <li>Build a number of income streams</li>
    <li>Align your spending with your values</li>
    <li>Track your spending</li>
    <li>Increase surplus income</li>
  </ul>
  <ul class="points" style="left:250px;width:150px">
    <li>Surplus income increases savings and equity</li>
    <li>Use savings and equity for investment</li>
    <li>Avoid borrowing for lifestyle assets / experiences where possible</li>
  </ul>
  <ul class="points" style="left:415px;width:172px">
    <li>Build an investment portfolio e.g. property and shares</li>
    <li>Use appropriate tax structures such as Family Trusts / Superannuation</li>
    <li>Invest for Growth or Income?</li>
    <li>Timing of tax deductions</li>
    <li>Depreciation</li>
  </ul>
  <ul class="points" style="left:597px;width:140px">
    <li>Insurance</li>
    <li>Contingency plans</li>
    <li>Diversification</li>
    <li>Focus on quality</li>
  </ul>
  <ul class="points" style="left:744px;width:152px">
    <li>Replacement of your salary or profits from running a business with income from your investment portfolio</li>
    <li>Drawing a sustainable income to maintain a great lifestyle and protect your retirement nest egg</li>
  </ul>
  <ul class="points" style="left:914px;width:150px">
    <li>Having a Will</li>
    <li>Power of Attorney</li>
    <li>Testamentary Trust?</li>
    <li>Guardianship</li>
  </ul>

  <svg class="band" viewBox="0 0 1092 14" aria-hidden="true">
    <polygon points="0,0 880,0 876,14 0,14" fill="var(--band)"/>
    <polygon points="1022,0 1092,0 1092,14 1018,14" fill="var(--band)"/>
  </svg>
  <div class="site">website to come</div>
</main>
</body>
</html>
```